Dental Office Needs a Flyer Design to Attract New Patients

We need a flyer design for a dental office in Rockville, MD, US. Our office name is Brightpath Dental Care. Our website is: brightpathdentalcare.example and our office logo can be seen on the website. We would like stay that call and make an appointment with Dr. Lena Okaru. The flyer can follow the color scheme of our logo (blue and white). We current have Holiday/New Year special: Dental exam, x-ray, and cleaning for $95 (a $300 value); please include this in the flyer. Also if you can include a winter inspired picture to be part of the flyer, that would be great. We really like your Grin Tallowby flyer design and are looking for something similar. Thank you!
Target Market(s)
Apartment complex that is 5 minutes (less than 1 mile away)
Industry/Entity Type
Dental
Look and feel

```html
<!DOCTYPE html>
<html lang="en">
<head>
<meta charset="utf-8">
<title>Brightpath Dental Care – Holiday / New Year Special</title>
<link rel="stylesheet" href="https://fonts.googleapis.com/css2?family=Oswald:wght@600&family=Dancing+Script:wght@500&family=Open+Sans:wght@400;600;700&display=swap">
<style>
  :root {
    --stage: #eceef2;
    --card: #f4f6fa;
    --ribbon: #2a32d8;
    --ribbon-dark: #171c96;
    --ribbon-fold: #10137a;
    --navy: #2b3a74;
    --teal: #3aa6c9;
    --logo: #3b8fa8;
    --snow-top: #f2f5f9;
    --snow-mid: #c9d3df;
    --snow-low: #e4eaf1;
    --white: #ffffff;
  }
  * { box-sizing: border-box; margin: 0; padding: 0; }
  html, body { width: 1200px; height: 939px; overflow: hidden; }
  body { background: var(--stage); font-family: "Open Sans", sans-serif; position: relative; }

  .flyer {
    position: absolute; left: 350px; top: 48px;
    width: 500px; height: 843px;
    background: var(--card);
    overflow: hidden;
    box-shadow: 0 6px 24px rgba(40, 50, 80, .18);
  }
  .winter-scene {
    position: absolute; left: 0; top: 150px; width: 100%; height: 420px;
    background: linear-gradient(180deg, var(--snow-top) 0%, var(--snow-mid) 45%, var(--snow-low) 80%, var(--card) 100%);
  }
  .brand {
    position: absolute; left: 0; top: 38px; width: 100%;
    display: flex; align-items: center; justify-content: center; gap: 14px;
  }
  .brand-dot { width: 34px; height: 34px; border-radius: 50%; background: var(--logo); }
  .brand-name { font-family: "Open Sans", sans-serif; font-weight: 700; font-size: 30px; color: var(--logo); letter-spacing: .5px; }

  .offer-ribbons { position: absolute; left: 0; top: 150px; width: 500px; height: 300px; overflow: visible; }
  .ribbon-face { fill: var(--ribbon); }
  .ribbon-tail { fill: var(--ribbon-dark); }
  .ribbon-fold { fill: var(--ribbon-fold); }
  .ribbon-script { font-family: "Dancing Script", cursive; font-size: 22px; fill: var(--white); }
  .ribbon-headline { font-family: "Oswald", sans-serif; font-weight: 600; font-size: 31px; fill: var(--white); letter-spacing: 1.5px; }
  .ribbon-price { font-family: "Oswald", sans-serif; font-weight: 600; font-size: 34px; fill: var(--white); }
  .ribbon-price-note { font-family: "Oswald", sans-serif; font-weight: 600; font-size: 17px; fill: var(--white); }

  .call-to-action {
    position: absolute; left: 0; top: 452px; width: 100%;
    text-align: center; color: var(--navy); font-size: 19px; line-height: 1.3;
  }
  .call-to-action strong { font-weight: 700; font-size: 23px; text-transform: uppercase; }

  .family-photo {
    position: absolute; left: 60px; top: 520px; width: 400px; height: 235px;
    background: radial-gradient(ellipse at 50% 45%, #e9c7a8 0%, #d9b597 35%, #c9d9e4 70%, rgba(244,246,250,0) 100%);
  }
  .contact { position: absolute; left: 0; top: 768px; width: 100%; text-align: center; }
  .contact-phone { font-size: 30px; color: var(--navy); font-weight: 400; line-height: 1.1; }
  .contact-web { font-size: 19px; color: var(--teal); font-weight: 400; }
</style>
</head>
<body>
  <article class="flyer">
    <div class="winter-scene" role="img" aria-label="Snow-covered winter trees with falling snowflakes"></div>

    <header class="brand">
      <span class="brand-dot"></span>
      <span class="brand-name">Brightpath Dental Care</span>
    </header>

    <svg class="offer-ribbons" viewBox="0 0 500 300" aria-label="Holiday/New Year special: dental exam, x-ray, and cleaning for $95 (a $300 value)">
      <g transform="rotate(-12 250 150)">
        <polygon class="ribbon-tail" points="40,45 125,45 125,100 40,100 62,72"/>
        <polygon class="ribbon-fold" points="105,100 125,100 125,112"/>
        <rect class="ribbon-face" x="105" y="22" width="230" height="78"/>
        <text class="ribbon-script" x="220" y="55" text-anchor="middle">Holiday/ New Year</text>
        <text class="ribbon-script" x="220" y="82" text-anchor="middle">special</text>

        <rect class="ribbon-face" x="30" y="110" width="430" height="92"/>
        <text class="ribbon-headline" x="245" y="148" text-anchor="middle">DENTAL EXAM,</text>
        <text class="ribbon-headline" x="245" y="188" text-anchor="middle">X-RAY, AND CLEANING</text>

        <polygon class="ribbon-tail" points="330,200 440,200 418,228 440,256 330,256"/>
        <polygon class="ribbon-fold" points="330,256 350,256 330,266"/>
        <rect class="ribbon-face" x="100" y="212" width="250" height="62"/>
        <text x="225" y="256" text-anchor="middle"><tspan class="ribbon-price">FOR $95 </tspan><tspan class="ribbon-price-note">(a $300 value)</tspan></text>
      </g>
    </svg>

    <p class="call-to-action">call and make an appointment<br>with <strong>Dr. Lena Okaru.</strong></p>

    <div class="family-photo" role="img" aria-label="Smiling family of four: parents with a girl and a boy on their backs"></div>

    <footer class="contact">
      <p class="contact-phone">(301) 555-0148</p>
      <p class="contact-web">brightpathdentalcare.example</p>
    </footer>
  </article>
</body>
</html>
```